International forest products consultancy needs a new brochure

We are a UK based international forest products consultancy (www.tarbeckfield.com) that needs a company brochure to share with new and potential clients. We have created an in-house version (see attachment) but feel that somebody else could do a much better job using better graphics!
We want the brochure to be A4 size so that we can print it internally. Ideally, somebody can design for us a template that fits with our brand and will allow us to update it in the future as/when we change our product portfolio. We currently use InDesign.
We would also be interested in having a long and short version. Perhaps a 16 page documents vs. just a 4 page document.
I have also attached some examples of recent reports we have published.
Can anybody help!
Target Market(s)
Senior management of international forest product companies, banks and logistical service providers
Industry/Entity Type
It Company

```html
<!DOCTYPE html>
<html lang="en">
<head>
<meta charset="utf-8">
<title>Fibreline - 12 issues per year</title>
<link href="https://fonts.googleapis.com/css2?family=Barlow:wght@400;500;600;700&display=swap" rel="stylesheet">
<style>
:root{
  --brand-blue:#1d5f95;
  --brand-blue-dark:#164d7c;
  --panel-grey:#e4e6e8;
  --thumb-grey:#c9ccd0;
  --ink:#3b3b3b;
  --rule:#9aa0a6;
  --white:#ffffff;
  --chart-red:#c0392b;
  --chart-green:#3d8a5a;
}
*{margin:0;padding:0;box-sizing:border-box}
html,body{width:848px;height:1200px;overflow:hidden;background:var(--white)}
body{font-family:"Barlow",Arial,sans-serif;color:var(--ink);position:relative}
.header-band{position:absolute;left:0;top:0;width:750px;height:160px;background:var(--brand-blue)}
.logo-box{position:absolute;left:518px;top:12px;width:195px;height:68px;background:var(--white);display:flex;align-items:center;justify-content:center;gap:8px}
.logo-box .mark{width:14px;height:14px;background:var(--brand-blue)}
.logo-box .name{font-size:28px;font-weight:600;color:var(--brand-blue)}
.page-title{position:absolute;left:76px;top:104px;color:var(--white);font-size:33px;font-weight:400;letter-spacing:.2px}
.page-title strong{font-weight:600}
.hero-photo{position:absolute;left:0;top:160px;width:398px;height:222px;background:linear-gradient(135deg,#4a4a4a 0%,#bdbdbd 35%,#f2f2f2 55%,#8a8a8a 80%,#3c3c3c 100%)}
.intro-panel{position:absolute;left:398px;top:160px;width:352px;height:222px;background:var(--panel-grey)}
.intro-panel p{position:absolute;left:32px;top:56px;width:290px;font-size:17px;line-height:22px;letter-spacing:.3px;color:var(--brand-blue)}
.sample-strip{position:absolute;left:65px;top:398px;width:685px;height:350px;background:var(--thumb-grey)}
.sample-page{position:absolute;top:6px;width:220px;height:338px;background:var(--white);overflow:hidden;font-size:5px;line-height:6px;color:#555}
.p1{left:5px}.p2{left:232px}.p3{left:460px}
.lines{position:absolute;background:repeating-linear-gradient(to bottom,#a9aeb3 0 1.2px,transparent 1.2px 3.6px)}
.s-head{position:absolute;font-size:4.5px;color:#555}
.s-logo{position:absolute;left:12px;top:24px;width:78px;height:26px;background:var(--brand-blue);color:var(--white);font-size:14px;font-weight:600;display:flex;align-items:center;padding-left:5px}
.s-title{position:absolute;color:var(--brand-blue);font-weight:700}
.s-box{position:absolute;border:.8px solid var(--rule)}
.s-tab{position:absolute;background:var(--brand-blue);color:var(--white);font-size:5px;font-weight:600;padding:1px 3px}
.body-copy{position:absolute;top:776px;font-size:12.6px;line-height:16px;letter-spacing:.25px;color:var(--ink)}
.body-copy p{margin-bottom:8px}
.col-1{left:65px;width:222px}
.col-2{left:303px;width:222px}
.col-3{left:540px;width:214px}
.info-box{position:absolute;left:538px;top:897px;width:224px;height:204px;background:var(--brand-blue-dark);color:var(--white);padding:12px 14px;font-size:12.6px;line-height:16px;font-weight:500;letter-spacing:.2px}
.info-box p{margin-bottom:4px}
.page-number{position:absolute;left:13px;top:1123px;width:34px;height:34px;border:1.5px solid var(--brand-blue);border-radius:50%;color:var(--brand-blue);font-size:16px;display:flex;align-items:center;justify-content:center}
</style>
</head>
<body>
<div class="header-band"></div>
<div class="logo-box"><span class="mark"></span><span class="name">Fibreline</span></div>
<h1 class="page-title"><strong>Fibreline</strong> - 12 issues per year</h1>

<div class="hero-photo" role="img" aria-label="Photograph of a large roll of pulp paper in a mill"></div>
<div class="intro-panel">
  <p>Fibreline is a monthly newsletter and dedicated website covering developments in the international pulp and paper markets.</p>
</div>

<section class="sample-strip" aria-label="Sample newsletter pages">
  <div class="sample-page p1">
    <div class="s-head" style="left:12px;top:8px;font-weight:700">TARBECKFIELD</div>
    <div class="s-head" style="left:150px;top:8px">Volume 20, No. 4</div>
    <div class="s-logo">Fibreline</div>
    <div class="s-head" style="left:96px;top:42px">Monthly review of the pulp market</div>
    <div class="s-title" style="left:12px;top:58px;width:198px;font-size:8px;line-height:9px">Softwood pulp prices move higher, widening the gap with hardwood</div>
    <div class="lines" style="left:12px;top:82px;width:62px;height:58px"></div>
    <div class="lines" style="left:80px;top:82px;width:130px;height:240px"></div>
    <div class="s-box" style="left:12px;top:148px;width:62px;height:118px">
      <div style="background:var(--brand-blue);color:#fff;font-size:4.5px;padding:1px 2px">Contents</div>
      <div class="lines" style="left:3px;top:12px;width:54px;height:100px"></div>
    </div>
    <div class="s-head" style="left:12px;top:272px;color:var(--brand-blue)">www.fibreline.com</div>
  </div>

  <div class="sample-page p2">
    <div class="s-tab" style="left:8px;top:7px">Fibreline</div>
    <div class="s-head" style="left:120px;top:8px">Volume 20, No. 4</div>
    <div class="s-title" style="left:8px;top:28px;font-size:7px">Printing &amp; writing paper, tissue markets</div>
    <svg style="position:absolute;left:8px;top:42px" width="56" height="280" viewBox="0 0 56 280">
      <g fill="none" stroke="#bbb" stroke-width=".6"><rect x="4" y="10" width="48" height="70"/><rect x="4" y="100" width="48" height="70"/><rect x="4" y="190" width="48" height="70"/></g>
      <polyline points="6,30 14,26 20,40 28,60 34,44 42,52 50,38" fill="none" stroke="var(--chart-red)" stroke-width="1"/>
      <polyline points="6,120 14,140 20,128 28,150 34,136 42,146 50,130" fill="none" stroke="var(--chart-red)" stroke-width="1"/>
      <polyline points="6,215 14,205 20,230 28,222 34,240 42,232 50,220" fill="none" stroke="var(--chart-red)" stroke-width="1"/>
    </svg>
    <div class="lines" style="left:72px;top:46px;width:140px;height:172px"></div>
    <svg style="position:absolute;left:72px;top:226px" width="140" height="90" viewBox="0 0 140 90">
      <rect x="2" y="2" width="136" height="86" fill="none" stroke="#bbb" stroke-width=".6"/>
      <polyline points="10,20 40,34 70,50 100,64 130,78" fill="none" stroke="var(--chart-red)" stroke-width="1.2"/>
      <g fill="var(--brand-blue)"><circle cx="22" cy="24" r="1.3"/><circle cx="48" cy="40" r="1.3"/><circle cx="66" cy="46" r="1.3"/><circle cx="90" cy="60" r="1.3"/><circle cx="118" cy="70" r="1.3"/></g>
    </svg>
  </div>

  <div class="sample-page p3">
    <div class="s-head" style="left:8px;top:8px">Volume 20, No. 4</div>
    <div class="s-tab" style="left:180px;top:7px">Fibreline</div>
    <div class="s-title" style="left:20px;top:38px;font-size:8px">Key statistics - China Analysis</div>
    <div class="lines" style="left:8px;top:56px;width:44px;height:150px"></div>
    <div class="s-box" style="left:58px;top:56px;width:154px;height:140px">
      <div style="background:var(--brand-blue);color:#fff;font-size:4.5px;padding:1px 2px">China imports of pulp by grade</div>
      <div class="lines" style="left:3px;top:12px;width:146px;height:124px"></div>
    </div>
    <svg style="position:absolute;left:58px;top:200px" width="154" height="110" viewBox="0 0 154 110">
      <rect x="1" y="1" width="152" height="108" fill="none" stroke="#bbb" stroke-width=".6"/>
      <path d="M8,100 L8,70 30,64 50,60 70,52 90,50 110,40 130,34 146,28 146,100Z" fill="var(--chart-green)"/>
      <path d="M8,100 L8,86 30,84 50,82 70,78 90,76 110,72 130,70 146,66 146,100Z" fill="var(--brand-blue)"/>
    </svg>
  </div>
</section>

<div class="body-copy col-1">
  <p>Ignis reriat. Dolecea vidello reiur?</p>
  <p>Archit dolorerume sitionsed quaspic aborepe liquas ese moluptas estio imusam nonsed es alignat ectem. Ut quatemporem et alitatet que perundite volectia volor aut quae. Itatur re, sam, sim natibus is aspelibusdam fugit, volum liqui volendi taquos maximentur, temqui tem quam fugiatibus molupta aliberr orerum exercit aditectam am hil inctorest quia voluptiae atur?</p>
  <p>Vit quae num am ut od quam rest as dolupta ectatur?</p>
  <p>Henes voloreris doloreh enihillabor adiaepudam sum rere nem volore, eum recestibus eveniasin nonet am ipsanime doluptat officiu samus, te laceprae sitiae nobit erum repta etur, oditatemquam exerum a de sequas nonet remo mos as vit voluptatatur modignisto volupta plat que ressit</p>
</div>
<div class="body-copy col-2">
  <p>alique nusapid quo volo ipsam nihil ipsunt explabo. Ga. Rem aut facepudant rerep Ignis reriat. Dolecea vidello reiur?</p>
  <p>Archit dolorerume sitionsed quaspic aborepe liquas ese moluptas estio imusam nonsed es alignat ectem. Ut quatemporem et alitatet que perundite volectia volor aut quae. Itatur re, sam, sim natibus is aspelibusdam fugit, volum liqui volenorepe liquas ese moluptas estio imusam nonsed es alignat ectem. Ut quatemporem et alitatet que perundite volectia volor aut quae. Itatur re, sam, sim natibus is adi taquos maximentur, temqui tem quam fugiatibus molupta aliberr orerum exercit aditectam am hil inctorest quia voluptiae atur?</p>
  <p>ium quunt pedionsequia nonet aut vella dionet as sinctis sed ex et qui</p>
</div>
<div class="body-copy col-3">
  <p>corem fuga. Ut maio consecu ptatati occullabore dit quamus.</p>
  <p>Ehene plit volum fugit volor rerro endae ea con ex et, aspienditis aditibu sciisse ctatur, sint. el id magnihil identitet apelistionse et et quo eos exerist apic testrum at estrum quasi</p>
</div>

<aside class="info-box">
  <p>ALL of the data published in Fibreline is available to subscribers in excel format. Most is available online at www.fibreline.com</p>
  <p>Data which is not published online is available on request.</p>
  <p>Price: from £1280/yr (single user) or £2500/yr (corporate user)</p>
  <p>More information: www.fibreline.com</p>
</aside>

<div class="page-number">4</div>
</body>
</html>
```